A standard Business and Stock Market Website

We are looking for a well designed and attractive website design which deals on the day to day business activities and stock market performance across the globe.

A good reference website for my proposed website is http://quillharbor.com and http://vkp.com

We are basically featuring the leading stock markets such as Pell marsh stock market and others. The Business name is Quarry lane.
I require very bright colors such as blue, green, black, golden.

Easy nagivating of the website is require and the design should also be responsive on mobile devices.

Designs for three pages. The first design should be for the home page, the second for the Economy/ stockmarkets, Third, business and tech. The home image would also feature stocks, economy, business, tech.

```html
<!DOCTYPE html>
<html lang="en">
<head>
<meta charset="utf-8">
<title>Quarry lane — Business &amp; Markets</title>
<link href="https://fonts.googleapis.com/css2?family=Montserrat:wght@400;500;600;700&family=Open+Sans:wght@400;600&display=swap" rel="stylesheet">
<style>
:root{
  --navy:#1b1f5c;
  --blue:#1f3f9e;
  --brand:#1a4c8f;
  --green:#6cc31e;
  --green-text:#5cb515;
  --red:#e3232b;
  --gold:#c9893a;
  --text:#3a3f4a;
  --muted:#9aa0a8;
  --line:#dcdfe3;
  --grey-bg:#f0f0f0;
  --beige:#e6d2bc;
  --beige-light:#f3e8dc;
  --chart-line:#b6dcf2;
}
*{box-sizing:border-box;margin:0;padding:0}
html,body{width:682px;height:1200px;overflow:hidden;background:#fff}
body{position:relative;font-family:"Open Sans",Arial,sans-serif;color:var(--text);font-size:8px}
.abs{position:absolute}
a{color:inherit;text-decoration:none}

.ticker{left:0;top:0;width:682px;height:22px;background:var(--navy);color:#fff;font:500 6px "Montserrat",sans-serif;display:flex;justify-content:space-between;align-items:center;padding:0 26px 0 82px}
.ticker .dn{color:#f26a1b}.ticker .up{color:var(--green)}

.hero{left:0;top:22px;width:682px;height:256px;background:linear-gradient(135deg,#1d3a92,#1a3aa0 50%,#14307e)}
.header{left:82px;top:33px;width:518px;height:20px;display:flex;align-items:center}
.logo{font:700 13px "Montserrat",sans-serif;color:#fff;display:flex;align-items:center;gap:5px;letter-spacing:-.2px}
.logo-dot{width:10px;height:10px;border-radius:50%;background:#fff}
.nav{margin-left:auto;display:flex;gap:12px;font:700 6.4px "Montserrat",sans-serif;color:#fff;align-items:center}
.btn{font:600 7px "Montserrat",sans-serif;border-radius:9px;height:15px;padding:0 8px;display:flex;align-items:center}
.btn-outline{border:1px solid var(--green);color:var(--green);margin-left:14px}
.btn-solid{background:var(--green);color:#fff;padding:0 12px;margin-left:4px}
.search{width:15px;height:15px;border:1px solid var(--green);border-radius:50%;margin-left:3px}
.header-rule{left:0;top:63px;width:682px;height:1px;background:rgba(255,255,255,.15)}

.chart-card{left:82px;top:87px;width:296px;height:169px;background:#fff}
.tabs{display:flex;height:20px;background:var(--green);font:500 9px "Montserrat",sans-serif}
.tab{padding:0 14px;display:flex;align-items:center;color:#d8f0bd}
.tab.active{background:#fff;color:var(--text)}
.chart-title{left:31px;top:37px;font:500 9.5px "Montserrat",sans-serif;color:var(--brand)}
.chart-note{left:0;width:296px;top:153px;text-align:center;font-size:6.5px;color:var(--muted)}

.hero-video{left:392px;top:87px;width:208px;height:169px;background:linear-gradient(160deg,#d9d7d0,#b8b6b0 60%,#6a6a70)}
.hero-caption{left:13px;bottom:13px;width:190px;font:700 10px/12px "Montserrat",sans-serif;color:#fff}

.play{width:46px;height:46px;border:3px solid #fff;border-radius:50%;display:flex;align-items:center;justify-content:center}
.play::after{content:"";border-left:14px solid #fff;border-top:9px solid transparent;border-bottom:9px solid transparent;margin-left:4px}
.play.sm{width:26px;height:26px;border-width:2px}
.play.sm::after{border-left-width:8px;border-top-width:5px;border-bottom-width:5px;margin-left:2px}

.col-title{font:700 8.5px "Montserrat",sans-serif;color:var(--text);text-transform:uppercase}
.photo{display:block}
.story{display:flex;gap:5px;font-size:7.4px;line-height:9.6px;padding-bottom:4px;border-bottom:1px solid var(--line);height:30px}
.story.active{color:var(--brand)}
.bullet{flex:none;width:7px;height:7px;border-radius:2px 2px 4px 4px;background:var(--brand);margin-top:1px}
.more{font-size:6.6px;color:var(--gold);text-align:right;padding:3px 0 3px;border-bottom:1px solid var(--line)}

.grey{left:0;top:548px;width:682px;height:270px;background:var(--grey-bg)}
.section-head{font:700 8.5px "Montserrat",sans-serif;text-transform:uppercase;border-top:1.5px solid #c9cdd2;border-bottom:1px solid #c9cdd2;padding:6px 0 4px}
.news{display:flex;gap:5px;font-size:7.6px;line-height:10px;height:43.5px}
.news.active{color:var(--brand)}
.news time{display:block;font-size:5.2px;color:var(--muted);margin-top:3px}

.main-video{left:258px;top:595px;width:253px;height:177px;background:linear-gradient(180deg,#8e2b34,#5a2a3a 40%,#2a2e48)}
.main-caption{left:13px;bottom:13px;width:230px;font:700 10px/12px "Montserrat",sans-serif;color:#fff}
.thumb{left:524px;width:76px;height:45px;display:flex;align-items:center;justify-content:center}
.thumb-cap{left:524px;width:76px;font-size:6px;line-height:6.8px;color:var(--text)}

.mkt-row{display:flex;align-items:center;height:20.5px;border-bottom:1px solid var(--line);font-size:7.6px}
.tag{font-size:4.8px;color:var(--gold);margin-left:6px;text-transform:uppercase;white-space:nowrap}
.pct{margin-left:auto;font:400 13px "Montserrat",sans-serif}
.pct.down{color:var(--red)}.pct.up{color:var(--green-text)}
.mini{font:600 4.6px/5.4px "Open Sans",sans-serif;margin-left:3px;width:24px}
.mini b{display:block;color:var(--red);font-weight:600}
.mini b.up{color:var(--green-text)}
.val{margin-left:auto;color:var(--green-text)}
.com-price{margin-left:auto;color:var(--gold);width:50px;text-align:right}
.com-chg{width:42px;text-align:right}
.com-chg.up{color:var(--green-text)}.com-chg.down{color:var(--red)}

.wave-band{left:0;top:970px;width:682px;height:63px;background:linear-gradient(180deg,#fff 0%,var(--beige-light) 40%,var(--beige) 100%)}

.foot-head{font:700 8.5px "Montserrat",sans-serif;color:var(--brand);padding-bottom:7px;border-bottom:1px solid var(--line);width:98px}
.foot-links{list-style:none;margin-top:8px;font:500 6.8px/13.5px "Montserrat",sans-serif;letter-spacing:.6px;color:var(--text)}
.foot-rule{left:82px;top:1158px;width:518px;height:1px;background:var(--line)}
.foot-logo{left:82px;top:1171px;font:700 12px "Montserrat",sans-serif;color:var(--brand);display:flex;align-items:center;gap:5px}
.foot-logo .logo-dot{background:var(--green)}
.copyright{left:0;width:682px;top:1176px;text-align:center;font:500 5.6px "Montserrat",sans-serif;color:var(--muted);letter-spacing:.3px}
.socials{left:550px;top:1171px;display:flex;gap:4px}
.social{width:14px;height:14px;border-radius:50%;background:var(--brand)}
</style>
</head>
<body>

<div class="abs ticker">
  <span>QLIA <span class="dn">▼</span> 19762.60 -0.29%</span>
  <span>QL 500 <span class="dn">▼</span> 2238.83 -0.46%</span>
  <span>TRADEX <span class="dn">▼</span> 5383.12 -0.90%</span>
  <span>CRUDE OIL <span class="up">▲</span> 53.89 0.22%</span>
  <span>EURO <span class="up">▲</span> 1.0519 0.27%</span>
</div>

<div class="abs hero"></div>
<header class="abs header">
  <div class="logo"><span class="logo-dot"></span>QUARRY LANE</div>
  <nav class="nav">
    <a href="#">HOME</a><a href="#">ECONOMY/STOCK MARKETS</a><a href="#">BUSINESS &amp; TECH</a><a href="#">NEWS</a>
  </nav>
  <a class="btn btn-outline" href="#">Sign up</a>
  <a class="btn btn-solid" href="#">Login</a>
  <span class="search"></span>
</header>
<div class="abs header-rule"></div>

<section class="abs chart-card">
  <div class="tabs"><span class="tab active">QLIA</span><span class="tab">QL 500</span><span class="tab">TRADEX</span></div>
  <div class="abs chart-title">QL INDUSTRIAL (I:QLI)</div>
  <svg class="abs" style="left:0;top:50px" width="296" height="100" viewBox="0 0 296 100">
    <g stroke="var(--chart-line)" stroke-width="1.2">
      <line x1="34" y1="8" x2="34" y2="80"/><line x1="41" y1="12" x2="41" y2="80"/><line x1="48" y1="14" x2="48" y2="80"/>
      <line x1="55" y1="12" x2="55" y2="80"/><line x1="62" y1="20" x2="62" y2="80"/><line x1="69" y1="16" x2="69" y2="80"/>
      <line x1="76" y1="18" x2="76" y2="80"/><line x1="83" y1="22" x2="83" y2="80"/><line x1="90" y1="8" x2="90" y2="80"/>
      <line x1="97" y1="12" x2="97" y2="80"/><line x1="104" y1="4" x2="104" y2="80"/><line x1="111" y1="10" x2="111" y2="80"/>
      <line x1="118" y1="14" x2="118" y2="80"/><line x1="125" y1="20" x2="125" y2="80"/><line x1="132" y1="24" x2="132" y2="80"/>
      <line x1="139" y1="18" x2="139" y2="80"/><line x1="146" y1="26" x2="146" y2="80"/><line x1="153" y1="24" x2="153" y2="80"/>
      <line x1="160" y1="22" x2="160" y2="80"/><line x1="167" y1="30" x2="167" y2="80"/><line x1="174" y1="28" x2="174" y2="80"/>
      <line x1="181" y1="32" x2="181" y2="80"/><line x1="188" y1="38" x2="188" y2="80"/><line x1="195" y1="30" x2="195" y2="80"/>
      <line x1="202" y1="40" x2="202" y2="80"/><line x1="209" y1="56" x2="209" y2="80"/><line x1="216" y1="62" x2="216" y2="80"/>
      <line x1="223" y1="50" x2="223" y2="80"/><line x1="230" y1="58" x2="230" y2="80"/><line x1="237" y1="48" x2="237" y2="80"/>
      <line x1="244" y1="30" x2="244" y2="80"/><line x1="251" y1="48" x2="251" y2="80"/>
    </g>
    <line x1="32" y1="10" x2="256" y2="10" stroke="#7cc7ea" stroke-width="0.8" stroke-dasharray="3 2"/>
    <polyline fill="none" stroke="var(--green)" stroke-width="1.3" points="32,12 36,8 41,12 48,14 55,12 62,20 69,16 76,18 83,22 90,8 97,12 104,4 111,10 118,14 125,20 132,24 139,18 146,26 153,24 160,22 167,30 174,28 181,32 188,38 195,30 202,40 209,56 216,62 223,50 230,58 237,48 241,46 244,30 251,48 254,46"/>
    <g font-family="Open Sans,sans-serif" font-size="6.2" fill="#555">
      <text x="258" y="6">19,820</text><text x="258" y="23">19,800</text><text x="258" y="40">19,780</text>
      <text x="258" y="57">19,760</text><text x="258" y="74">19,740</text>
      <text x="28" y="91">9:3</text><text x="77" y="91">11:11</text><text x="124" y="91">12:52</text>
      <text x="172" y="91">14:33</text><text x="220" y="91">16:15</text>
    </g>
  </svg>
  <div class="abs chart-note">Chart data delayed 20 mins</div>
</section>

<section class="abs hero-video" role="img" aria-label="Video still: businessman presenting at a whiteboard with sketched charts">
  <div class="abs play" style="left:81px;top:62px"></div>
  <div class="abs hero-caption">Lorem ipsum dolor consectetur sed do eiusmod tempor.</div>
</section>

<section class="abs" style="left:81px;top:309px;width:165px">
  <h2 class="col-title">Economy</h2>
  <div class="photo" role="img" aria-label="Photo of a compass with a flag pointing to the word economy" style="margin-top:5px;height:90px;background:linear-gradient(160deg,#eeeeee,#c9c9c9 60%,#8e8680)"></div>
  <div style="margin-top:9px">
    <div class="story active"><span class="bullet"></span>Molore eu fugiat nulla pariatur esse excepteur sint occaecat</div>
    <div class="story"><span class="bullet"></span>Duis aute irure dolor in reprehend in voluptate velit esse cillum</div>
    <div class="story"><span class="bullet"></span>Molore eu fugiat nulla pariatur esse excepteur sint occaecat</div>
    <div class="more">More News ›</div>
  </div>
</section>
<section class="abs" style="left:258px;top:309px;width:164px">
  <h2 class="col-title">Business</h2>
  <div class="photo" role="img" aria-label="Photo of cars in a showroom" style="margin-top:5px;height:90px;background:linear-gradient(180deg,#5c6470,#b7bcc4 50%,#e8e8ea)"></div>
  <div style="margin-top:9px">
    <div class="story"><span class="bullet"></span>Molore eu fugiat nulla pariatur esse excepteur sint occaecat</div>
    <div class="story"><span class="bullet"></span>Duis aute irure dolor in reprehend in voluptate velit esse cillum</div>
    <div class="story"><span class="bullet"></span>Molore eu fugiat nulla pariatur esse excepteur sint occaecat</div>
    <div class="more">More News ›</div>
  </div>
</section>
<section class="abs" style="left:436px;top:309px;width:164px">
  <h2 class="col-title">Tech</h2>
  <div class="photo" role="img" aria-label="Photo of hands using a laptop on a wooden desk" style="margin-top:5px;height:90px;background:linear-gradient(135deg,#3a3430,#6c5a4a 50%,#9aa0a4)"></div>
  <div style="margin-top:9px">
    <div class="story"><span class="bullet"></span>Molore eu fugiat nulla pariatur esse excepteur sint occaecat</div>
    <div class="story"><span class="bullet"></span>Duis aute irure dolor in reprehend in voluptate velit esse cillum</div>
    <div class="story"><span class="bullet"></span>Molore eu fugiat nulla pariatur esse excepteur sint occaecat</div>
    <div class="more">More News ›</div>
  </div>
</section>

<div class="abs grey"></div>
<section class="abs" style="left:81px;top:584px;width:165px">
  <h2 class="section-head">Latest News</h2>
  <div style="margin-top:8px">
    <div class="news active"><span class="bullet"></span><div>Duis aute irure dolor in reprehend in voluptate velit esse cillum<time>31.12.2016, 9.00 a.m</time></div></div>
    <div class="news"><span class="bullet"></span><div>Molore eu fugiat nulla pariatur esse excepteur sint occaecat<time>31.12.2016, 9.00 a.m</time></div></div>
    <div class="news"><span class="bullet"></span><div>Duis aute irure dolor in reprehend in voluptate velit esse cillum<time>31.12.2016, 9.00 a.m</time></div></div>
    <div class="news"><span class="bullet"></span><div>Molore eu fugiat nulla pariatur esse excepteur sint occaecat<time>31.12.2016, 9.00 a.m</time></div></div>
  </div>
  <div class="abs" style="right:0;top:188px;font-size:6.6px;color:var(--gold)">More News ›</div>
</section>

<h2 class="abs col-title" style="left:259px;top:583px">Video</h2>
<section class="abs main-video" role="img" aria-label="Video still: speaker at a podium in front of flags">
  <div class="abs play" style="left:103px;top:65px"></div>
  <div class="abs main-caption">Lorem ipsum dolor sit amet, consectetur sed do eiusmod tempor incididunt.</div>
</section>
<div class="abs" style="left:464px;top:779px;font-size:6.6px;color:var(--gold)">More Videos ›</div>

<div class="abs thumb" style="top:595px;background:linear-gradient(135deg,#3b5a7a,#1e2a3a)" role="img" aria-label="Video thumbnail: business presentation"><span class="play sm"></span></div>
<div class="abs thumb-cap" style="top:642px">Molore eu fugiat nulla pariatur esse</div>
<div class="abs thumb" style="top:661px;background:linear-gradient(135deg,#8e2b34,#2a2e48);outline:2px solid #2a6fd0" role="img" aria-label="Video thumbnail: speaker at a podium"><span class="play sm"></span></div>
<div class="abs thumb-cap" style="top:708px">Molore eu fugiat nulla pariatur esse</div>
<div class="abs thumb" style="top:727px;background:linear-gradient(180deg,#9aa6b4,#6a5a48)" role="img" aria-label="Video thumbnail: construction workers on a site"><span class="play sm"></span></div>
<div class="abs thumb-cap" style="top:774px">Molore eu fugiat nulla pariatur esse</div>

<section class="abs" style="left:81px;top:849px;width:165px">
  <h2 class="section-head">World Markets</h2>
  <div style="margin-top:6px">
    <div class="mkt-row">Japan<span class="tag">Kiso 225</span><span class="pct down">-0.16%</span><span class="mini">19,114.37<b>-40.72</b></span></div>
    <div class="mkt-row">London<span class="tag">Thame 100</span><span class="pct up">+0.47%</span><span class="mini">19,114.37<b class="up">+40.72</b></span></div>
    <div class="mkt-row">Hong Kong<span class="tag">Harbor Idx</span><span class="pct up">+0.27%</span><span class="mini">19,114.37<b class="up">+40.72</b></span></div>
    <div class="mkt-row">Germany<span class="tag">Rhein</span><span class="pct up">+0.57%</span><span class="mini">19,114.37<b class="up">+40.72</b></span></div>
  </div>
</section>
<section class="abs" style="left:258px;top:849px;width:164px">
  <h2 class="section-head">Currencies</h2>
  <div style="margin-top:6px">
    <div class="mkt-row">Euro<span class="val">$1.05</span></div>
    <div class="mkt-row">British Pound<span class="val">$1.23</span></div>
    <div class="mkt-row">Japanese Yen<span class="val">¥117.00</span></div>
    <div class="mkt-row">Canadian Dollar<span class="val">$0.74</span></div>
  </div>
</section>
<section class="abs" style="left:436px;top:849px;width:164px">
  <h2 class="section-head">Commodities</h2>
  <div style="margin-top:6px">
    <div class="mkt-row">Oil<span class="com-price">$53.89</span><span class="com-chg up">+0.32%</span></div>
    <div class="mkt-row">Gas<span class="com-price">$3.74</span><span class="com-chg up">+0.54%</span></div>
    <div class="mkt-row">Gold<span class="com-price">$1,152.00</span><span class="com-chg down">-0.18%</span></div>
    <div class="mkt-row">Silver<span class="com-price">$15.96</span><span class="com-chg down">-0.28%</span></div>
  </div>
</section>

<div class="abs wave-band" role="img" aria-label="Decorative band of soft beige hills with a market line motif"></div>

<footer>
  <div class="abs" style="left:82px;top:1059px">
    <h3 class="foot-head">Useful links</h3>
    <ul class="foot-links"><li>Home</li><li>Economy/Stock Markets</li><li>Busines &amp; Tech</li><li>News</li></ul>
  </div>
  <div class="abs" style="left:299px;top:1059px">
    <h3 class="foot-head">Customer Services</h3>
    <ul class="foot-links"><li>Need help</li><li>Customer Center</li><li>Login</li><li>My account</li></ul>
  </div>
  <div class="abs" style="left:502px;top:1059px">
    <h3 class="foot-head">Ads</h3>
    <ul class="foot-links"><li>Advertise</li><li>Place an Ad</li><li>Sell Your Business</li><li>Career</li></ul>
  </div>
  <div class="abs foot-rule"></div>
  <div class="abs foot-logo"><span class="logo-dot"></span>QUARRY LANE</div>
  <div class="abs copyright">Copyright 2017 © Quarry lane - All Rights Reserved</div>
  <div class="abs socials"><span class="social"></span><span class="social"></span><span class="social"></span></div>
</footer>

</body>
</html>
```